Kelvane Plumbing Business cards

Company is Kelvane Plumbing.
name Dashel Morrowby, I am a plumber, drainer, gasfitter and roofer
Mobile: 0431 906 154
Email address: info@kelvaneplumbing.example (check out my website for some ideas)
Website: www.kelvaneplumbing.example
ABN: 82 916 203 471
LIC: 604517K

I am reliable all round plumber. I am a 24 hour emergency service. Kelvane Plumbing is a professional plumbing service in the Illawarra, South Coast, Southern Sydney and Southern Highland regions of NSW. We offer a 24 hour emergency service for piece of mind to our customers. Call us now to see how we can help you. Kelvane Plumbing approaches every job with attention to detail and excellent customer service. With our superior workmanship you can be confident that the job will be done right the first time around. You can rest assured with results that are guaranteed to last.

Target Market(s)

the general public

Contact Information for Business Card

look up website for some ideas something with similar colours to logo and new modern and to catch the eye.

Colors
fdfdfd
ffffff
000000
7f7f7f
aaaaaa
33a6d7
0492cd

Requirements
Must have
• all contact details
• company- Kelvane Plumbing
• name- Dashel Morrowby
• number mobile- 0431 906 154
• Email address- info@kelvaneplumbing.example
• Website- www.kelvaneplumbing.example
• ABN- 82 916 203 471
• LIC- 604517K

```html
<!DOCTYPE html>
<html lang="en">
<head>
<meta charset="utf-8">
<title>Kelvane Plumbing – Business Cards</title>
<link rel="stylesheet" href="https://fonts.googleapis.com/css2?family=Roboto:wght@400;500&family=Roboto+Condensed:wght@500&display=swap">
<style>
  :root {
    --bg: #e6e6e6;
    --card: #000000;
    --blue: #0492cd;
    --blue-light: #33a6d7;
    --grey: #7f7f7f;
    --grey-light: #aaaaaa;
    --white: #ffffff;
  }
  * { box-sizing: border-box; margin: 0; padding: 0; }
  html, body {
    width: 1125px;
    height: 1200px;
    overflow: hidden;
    background: var(--bg);
  }
  .canvas {
    position: relative;
    width: 1125px;
    height: 1200px;
  }
  .card {
    position: absolute;
    left: 171px;
    width: 826px;
    height: 470px;
    background: var(--card);
    box-shadow: 0 3px 10px rgba(0,0,0,0.35);
    overflow: hidden;
  }
  .card--front { top: 106px; }
  .card--back { top: 640px; }

  .name-band {
    position: absolute;
    left: 0; top: 0;
    width: 100%;
    height: 82px;
    background: var(--blue);
    display: flex;
    align-items: center;
    justify-content: center;
  }
  .holder-name {
    font-family: "Roboto Condensed", sans-serif;
    font-weight: 500;
    font-size: 31px;
    color: var(--white);
    letter-spacing: 0.01em;
    text-transform: uppercase;
  }
  .pipe-line {
    position: absolute;
    left: 73px; top: 82px;
    right: 0;
    height: 5px;
    background: var(--grey);
  }

  .company-name {
    position: absolute;
    left: 69px;
    top: 245px;
    width: 360px;
    font-family: "Roboto", sans-serif;
    font-weight: 500;
    font-size: 34px;
    color: var(--blue);
    white-space: nowrap;
  }

  .divider {
    position: absolute;
    left: 446px;
    top: 198px;
    width: 2px;
    height: 130px;
    background: linear-gradient(to bottom, rgba(170,170,170,0), var(--grey-light) 30%, var(--grey-light) 70%, rgba(170,170,170,0));
  }

  .contact {
    position: absolute;
    left: 481px;
    top: 196px;
    list-style: none;
    font-family: "Roboto", sans-serif;
    font-size: 20px;
    color: var(--white);
    line-height: 26px;
  }
  .contact__item {
    display: flex;
    align-items: center;
    gap: 12px;
  }
  .contact__icon {
    width: 18px;
    height: 18px;
    flex: none;
    fill: var(--blue);
  }
  .contact__item--plain { margin-top: 6px; }
  .contact__item--plain + .contact__item--plain { margin-top: 0; }

  .back-name {
    position: absolute;
    left: 0; right: 0;
    top: 212px;
    text-align: center;
    font-family: "Roboto", sans-serif;
    font-weight: 500;
    font-size: 40px;
    color: var(--blue);
  }
  .back-web {
    position: absolute;
    left: 0; right: 0;
    top: 410px;
    text-align: center;
    font-family: "Roboto", sans-serif;
    font-size: 19px;
    letter-spacing: 0.36em;
    color: var(--white);
  }
</style>
</head>
<body>
<main class="canvas">
  <section class="card card--front">
    <header class="name-band"><h1 class="holder-name">Dashel Morrowby</h1></header>
    <div class="pipe-line"></div>

    <p class="company-name">Kelvane Plumbing</p>

    <div class="divider"></div>

    <ul class="contact">
      <li class="contact__item">
        <svg class="contact__icon" viewBox="0 0 24 24" aria-hidden="true"><path d="M6.6 10.8a15.1 15.1 0 0 0 6.6 6.6l2.2-2.2a1 1 0 0 1 1-.25 11.4 11.4 0 0 0 3.6.57 1 1 0 0 1 1 1V20a1 1 0 0 1-1 1A17 17 0 0 1 3 4a1 1 0 0 1 1-1h3.5a1 1 0 0 1 1 1c0 1.25.2 2.45.57 3.57a1 1 0 0 1-.25 1z"/></svg>
        <span>0431 906 154</span>
      </li>
      <li class="contact__item">
        <svg class="contact__icon" viewBox="0 0 24 24" aria-hidden="true"><path d="M2 5h20v14H2z" /><path d="M2 5l10 8 10-8" fill="none" stroke="#000" stroke-width="1.8"/></svg>
        <span>info@kelvaneplumbing.example</span>
      </li>
      <li class="contact__item">
        <svg class="contact__icon" viewBox="0 0 24 24" aria-hidden="true"><circle cx="12" cy="12" r="10"/><path d="M2 12h20M12 2c3 3 3 17 0 20M12 2c-3 3-3 17 0 20" fill="none" stroke="#000" stroke-width="1.5"/></svg>
        <span>www.kelvaneplumbing.example</span>
      </li>
      <li class="contact__item contact__item--plain">ABN- 82 916 203 471</li>
      <li class="contact__item contact__item--plain">LIC- 604517K</li>
    </ul>
  </section>

  <section class="card card--back">
    <p class="back-name">Kelvane Plumbing</p>
    <p class="back-web">www.kelvaneplumbing.example</p>
  </section>
</main>
</body>
</html>
```